Harrowgate Estates Business Card for Apartment Buildings

Create business cards for resident managers who run apartment buildings. The audience is the public who are searching for apartment rentals, and current residents who live at the apartment building. Key design element will be incorporating the company logo, however, the logo cannot dominate. The building name and manager name are more important than the logo. Current business card design leaves little room for copy, so we may need to reduce the size on the current card to allow for more space for copy.

Target Market(s)

Adults 18-65 years of age, who are looking for an apartment rental, plus current residents who live at our apartment buildings.

Industry/Entity Type

Property Management

Contact Information for Business Card

A major design element will be use of the company logo. Important property and manager contact information must be part of the design. The size of the logo will need to be reduced to make room for building and manager contact copy.

Font styles to use
Sans Serif

Colors
3176b5
000000
959595
ffffff

Requirements
Must have
• 1) Incorporate the company logo.
• 2) Use the company colors (dark blue, black/grey, over white).
• 3) FEATURE THE BUILDING NAME
• 4) FEATURE THE MANAGER NAME
• 5) The company name is less important than BUILDING and MANAGER
• 6) Manager contact information
• **SEE ATTACHED CREATIVE BRIEF**
Nice to have
• 1) Back of card logo watermark
• 2) Ability to write notes on back of carfd
Should not have
• Avoid letting the company logo dominate the card, the building name and manager are more important than the company logo.

```html
<!DOCTYPE html>
<html lang="en">
<head>
<meta charset="utf-8">
<title>Harrowgate Estates – Resident Manager Business Card</title>
<link rel="stylesheet" href="https://fonts.googleapis.com/css2?family=Oswald:wght@500&family=Open+Sans:wght@400&family=Tinos:ital@1&display=swap">
<style>
  :root {
    --brand-blue: #1f6dac;
    --ink: #2b2b2b;
    --grey: #959595;
    --paper: #ffffff;
    --backdrop: #e6e6e6;
    --rule-blue: #3176b5;
    --notes-border: #bdbdbd;
  }
  * { margin: 0; padding: 0; box-sizing: border-box; }
  html, body { width: 1007px; height: 1200px; overflow: hidden; }
  body { background: var(--backdrop); position: relative; font-family: "Open Sans", Arial, sans-serif; }

  .card {
    position: absolute;
    left: 77px;
    width: 813px;
    height: 470px;
    background: var(--paper);
    overflow: hidden;
    box-shadow: 0 2px 8px rgba(0,0,0,.15);
  }
  .card--back { top: 75px; }
  .card--front { top: 622px; height: 468px; }

  /* Back */
  .back-texture {
    position: absolute; inset: 0;
    background: linear-gradient(100deg, #d9d9d9 0%, #f2f2f2 18%, #fafafa 45%, #efefef 75%, #e0e0e0 100%);
  }
  .company-name {
    position: absolute;
    top: 52px; left: 0; right: 0;
    display: flex; align-items: center; justify-content: center; gap: 14px;
    font-family: "Oswald", Arial, sans-serif;
    font-weight: 500;
    font-size: 40px;
    letter-spacing: 1px;
    color: var(--brand-blue);
    text-transform: uppercase;
  }
  .company-name .mark { width: 26px; height: 26px; background: var(--brand-blue); }

  .notes {
    position: absolute;
    left: 56px; top: 144px;
    width: 704px; height: 288px;
    background: var(--paper);
    border: 2px solid var(--notes-border);
    padding: 0 12px;
  }
  .notes__line { height: 43px; border-bottom: 2px solid var(--rule-blue); }
  .notes__line:first-child { height: 41px; }

  /* Front */
  .property { position: absolute; right: 42px; top: 18px; text-align: right; }
  .property__name {
    font-family: "Oswald", Arial, sans-serif;
    font-weight: 500; font-size: 40px; line-height: 1.1;
    color: var(--brand-blue); text-transform: uppercase; letter-spacing: .5px;
  }
  .property__address { font-size: 21px; color: var(--ink); margin-top: 2px; }

  .manager { position: absolute; right: 42px; top: 164px; text-align: right; }
  .manager__name {
    font-family: "Oswald", Arial, sans-serif;
    font-weight: 500; font-size: 38px; line-height: 1.1;
    color: var(--brand-blue); text-transform: uppercase; letter-spacing: .5px;
  }
  .manager__title {
    font-family: "Tinos", "Times New Roman", serif;
    font-style: italic; font-size: 34px; color: var(--ink); line-height: 1.1;
  }

  .contact {
    position: absolute; right: 42px; top: 286px;
    list-style: none; text-align: right;
    font-size: 19px; line-height: 23px; color: var(--brand-blue);
  }

  .front-brand {
    position: absolute; left: 24px; top: 200px;
    display: flex; align-items: center; gap: 14px;
    font-family: "Oswald", Arial, sans-serif;
    font-weight: 500; font-size: 34px; line-height: 1.05;
    color: var(--brand-blue); text-transform: uppercase;
  }
  .front-brand .mark { width: 40px; height: 40px; background: var(--brand-blue); flex: none; }

  .footer-band {
    position: absolute; left: 0; right: 0; bottom: 0;
    height: 58px; background: var(--brand-blue);
  }
</style>
</head>
<body>

  <section class="card card--back" aria-label="Card back">
    <div class="back-texture" role="img" aria-label="Soft grey architectural columns backdrop"></div>
    <div class="company-name"><span class="mark"></span>Harrowgate Estates LLC</div>
    <div class="notes" aria-label="Notes area">
      <div class="notes__line"></div>
      <div class="notes__line"></div>
      <div class="notes__line"></div>
      <div class="notes__line"></div>
      <div class="notes__line"></div>
      <div class="notes__line"></div>
    </div>
  </section>

  <section class="card card--front" aria-label="Card front">
    <div class="property">
      <h1 class="property__name">Linden Court Apartments</h1>
      <p class="property__address">4820 Marigold Avenue - San Diego, CA 92105</p>
    </div>

    <div class="front-brand"><span class="mark"></span><span>Harrowgate<br>Estates</span></div>

    <div class="manager">
      <h2 class="manager__name">Marisol Delgado</h2>
      <p class="manager__title">Resident Manager</p>
    </div>

    <ul class="contact">
      <li>OFFICE: 555-201-4830</li>
      <li>FAX: 555-201-4831</li>
      <li>CELL: 555-318-6274</li>
      <li>EMAIL: marisol@harrowgateestates.com</li>
    </ul>

    <div class="footer-band"></div>
  </section>

</body>
</html>
```